Meridel Wellness Website Meridel Verdant Remedial Products/Services, Ecommerce, Appt Book

We at MeridelWellness.example need a clean website home and interior pages designed for our luxury all-natural and prescription drug-FREE brand, Meridel Verdant Remedials.

Meridel Verdant Remedials
Rooted In Stillwood
Est. Aspen, Colorado

We deliver phytoncide and plant medicines as well as essential oils, vitamins, supplements, minerals, herbs, other skin, cosmetic, beauty products, products for the home and office, pet products and health products along with the following services :
nutrition counseling
nutrient therapy
herbalism
herbalism formulas

What differentiates Meridel Wellness is our exclusive
forest therapy
nature therapy
ski therapy
white water rafting therapy
golf therapy
equine therapy
and other high end recreational therapy solutions in Aspen and Vail Colorado.

We also offer luxury nature themed retreats and glamping (glamourous luxury camping) retreats in Aspen, Vail, California and Hawaii

And deliver all-natural plant based therapeutic treatments to heal, reverse or prevent mental illness and drug or alcohol addictions

We are HQ in Aspen Colorado with locations in Vail, California, Hawaii ...

The store and products is a subsidiary of CortlandClinicians.example

We heal, reverse and prevent chronic illness and disease naturally without pharmaceutical drugs of any kind. Our main firm is a concierge medical firm which offers concierge medical services to high net worth clients, executives, families, kids and corporations.

Colors to use :

White (lots of white space, clean, luxury, pure, healing)
Green (paying homage to our therapeutic remedies trees, plants, forests)
Shiny Silver/Platinum/Chrome (think Halden Marque logo)

Here are the main links for the website :

Meridel Wellness Store

Nutrition & Nutrient Therapy
Herbal Apothecary
Vitamins, Minerals and Supplements
Forest, Ski, Surf , Golf, Equine Therapy
Luxury Health Retreats
Glamping Health Camps
Contact
About
Blog

Home page and interior pages design
Will have a ecommerce to purchase the products direct
Will have an appointment booking section for recreational therapy or nutrition or herbalism consults
Will have an online consultation booking section
Will have a retreat/vacation/camp reservation page

Target Market(s)

Luxury and high net-worth or wealthy health conscious consumers, natural health consumers, concierge consumers, Nutrition and outdoor recreation consumers , Aspen and Vail travelers, skiers, golfers, hikers, white water rafting enthusiasts, executives/ceo's and retirees as well as those individuals including kids interested in nature, hiking, ski, camping luxury camps (glamping) ... All services are all concierge level and we cater those who need natural sustainable cures for everything from mental health, senior health, impotence, weight loss/weight management, fatigue/low energy, hormonal balance for men and women etc.

Coding

Coded - Design and coding required

Number of Pages Required

5+ page

Requirements
Must have
• Use same consistent font and colors as the brand. See attachments.
• Must have a main gallery on the home page where we will cycle thru images of our products, images of the forests, wildlife and video experiences ...
• Please use consistent fonts and the colors should be white, green (plants/trees/especially forests) and platinum/shiny chrome/silver)
• Trees from the aspen forests b/c all of our products are created from nature, plants and phytoncides. Phytoncides are substances emitted from plants and trees. These substances have natural healing powers to eliminate stress, kill cancer cells, lower blood pressure, improve immune functioning, etc.
• You can get a great visual checking out the images (and take what you need for the main gallery on the site) at our twitter feed, see images @meridelwellness
• We will later request that you do markup of psd files to htiml
• This site will be most likely done in wordpress
Nice to have
• We also offer online consultations so it would be good to add some type of video link or chat feature, a sneak peak of our twitter feed from @meridelwellness and the footer can look similar to the one we have a cortlandclinicians.example
Should not have
• No other colors outside of our current branding choices

```html
<!DOCTYPE html>
<html lang="en">
<head>
<meta charset="utf-8">
<title>Meridel Wellness</title>
<link href="https://fonts.googleapis.com/css2?family=Cinzel:wght@400;700&family=Open+Sans:wght@400;600;700&display=swap" rel="stylesheet">
<style>
:root{
  --green:#7cb82f;
  --green-dark:#5f9a1c;
  --white:#ffffff;
  --ink:#2c2c2c;
  --text:#6f6f6f;
  --rail:#9a9a9a;
  --rail-line:#ababab;
  --rail-head:#262626;
  --silver:#d9d9d9;
  --card-foot:#ededed;
  --footer:#2b2b2b;
}
*{box-sizing:border-box;margin:0;padding:0}
html,body{width:1200px;height:3309px;overflow:hidden;background:var(--white)}
body{position:relative;font-family:"Open Sans",Arial,sans-serif;color:var(--text)}
.abs{position:absolute}

/* header */
.topline{left:0;top:0;width:1200px;height:4px;background:var(--green)}
.brand{left:48px;top:24px;display:flex;align-items:center;gap:12px}
.brand-square{width:36px;height:40px;background:linear-gradient(135deg,#f2f2f2,#b9b9b9 55%,#e6e6e6)}
.brand-name{font-family:"Cinzel",Georgia,serif;font-size:17px;color:var(--ink)}
.contacts{left:624px;top:16px;display:flex;align-items:center;height:30px;font-size:12px;color:var(--ink)}
.social-dot{width:28px;height:28px;border-radius:50%;margin-right:6px}
.contact-item{display:flex;align-items:center;gap:8px;margin-left:20px}
.main-nav{left:302px;top:60px;width:830px;display:flex;justify-content:space-between;font-size:12.5px;color:var(--ink);white-space:nowrap}
.main-nav .active{color:var(--green)}
.search{left:1144px;top:62px}

/* side rail */
.rail{left:0;top:100px;width:287px;height:1810px;background:var(--rail)}
.rail-head{position:absolute;left:0;width:287px;height:34px;background:var(--rail-head);color:#fff;font-family:"Cinzel",Georgia,serif;font-size:15px;letter-spacing:1px;padding:8px 0 0 22px}
.rail-list{position:absolute;left:0;width:287px;list-style:none}
.rail-list li{height:31px;line-height:31px;padding-left:20px;font-size:11.5px;color:#fff;border-bottom:1px solid var(--rail-line)}
.rail-video{left:0;top:909px;width:287px;height:195px;background:
  linear-gradient(180deg,#8e9ea6 0,#6f848c 18%,#2f4a38 34%,#1f3a28 48%,#3f5d66 56%,#6b8a92 64%,#3a5a46 78%,#14241a 100%)}
.rail-video-title{left:18px;top:914px;font-size:13px;color:#fff}
.rail-video-tools{left:232px;top:914px}
.play{left:126px;top:990px}
.rail-promo{left:0;top:1118px;width:287px;height:200px;background:
  radial-gradient(ellipse 60px 90px at 205px 90px,#f4efe6 0,rgba(244,239,230,0) 100%),
  linear-gradient(180deg,#d8e6c4 0,#b9d08e 45%,#9dbb4e 70%,#d8c441 88%,#8fae3c 100%)}
.rail-promo-panel{left:0;top:1118px;width:150px;height:200px;background:var(--green)}
.rail-promo-text{left:12px;top:1128px;width:132px;font-size:14px;font-weight:700;line-height:24px;color:#fff}

/* hero */
.hero{left:287px;top:100px;width:913px;height:430px;background:
  radial-gradient(ellipse 180px 110px at 600px 200px,#c7348f 0,rgba(199,52,143,.35) 30%,rgba(255,255,255,0) 70%),
  radial-gradient(ellipse 70px 40px at 600px 175px,#f2d63a 0,rgba(242,214,58,0) 100%),
  radial-gradient(ellipse 330px 200px at 350px 130px,#ffffff 0,#f4f3f6 40%,rgba(244,243,246,0) 100%),
  radial-gradient(ellipse 300px 170px at 720px 380px,#ffffff 0,#eeecf1 45%,rgba(238,236,241,0) 100%),
  linear-gradient(135deg,#9fa8b2 0,#d8d6de 35%,#c9c6d0 60%,#8b95a0 100%)}
.hero-title{right:100px;top:318px;text-align:right;font-family:"Cinzel",Georgia,serif;font-size:38px;line-height:44px;color:#fff;text-shadow:0 1px 4px rgba(0,0,0,.35)}
.hero-title.dark{color:var(--ink);text-shadow:none}
.dots{left:1016px;top:490px;display:flex;gap:10px}
.dots span{width:11px;height:11px;border-radius:50%;background:#fff}
.dots span:first-child{background:var(--green)}

.badge{width:34px;height:42px;background:linear-gradient(135deg,#f4f4f4,#b5b5b5 55%,#e4e4e4);border:3px solid #fff;box-shadow:0 1px 3px rgba(0,0,0,.25)}
.section-title{font-family:"Cinzel",Georgia,serif;color:var(--ink);text-align:center;width:913px;left:287px}
.rule{left:287px;width:913px;height:1px;background:#e4e4e4}

/* welcome */
.welcome-text{left:377px;width:733px;text-align:center;font-size:12px;line-height:22px}

/* services */
.service{width:200px;text-align:center}
.service-icon{margin:0 auto;width:84px;height:84px;border-radius:50%;background:var(--green);border:4px solid #fff;box-shadow:0 0 0 3px var(--green)}
.service-name{margin-top:20px;font-family:"Cinzel",Georgia,serif;font-size:13px;font-weight:700;color:var(--ink);line-height:18px}
.service-copy{margin-top:12px;font-size:11.5px;line-height:20px}
.read-more{margin-top:14px;font-size:11.5px;font-weight:700;color:var(--green)}

/* products */
.card{width:194px;border:1px solid #e3e3e3;background:#fff;overflow:hidden}
.card-photo{height:160px}
.photo-bottle{background:radial-gradient(ellipse 40px 56px at 97px 84px,#ffffff 0,#e4e4e4 70%,rgba(228,228,228,0) 100%),radial-gradient(ellipse 110px 30px at 97px 140px,#d8d8d4 0,rgba(216,216,212,0) 100%),#fbfbf9}
.photo-jar{background:radial-gradient(ellipse 28px 40px at 97px 92px,#ffffff 0,#e2e2e2 70%,rgba(226,226,226,0) 100%),radial-gradient(ellipse 90px 24px at 97px 140px,#dadad6 0,rgba(218,218,214,0) 100%),#fbfbf9}
.photo-box{background:linear-gradient(160deg,rgba(255,255,255,0) 20%,#f7f7f4 22%,#ecece8 60%,rgba(236,236,232,0) 62%),#fbfbf9}
.photo-dropper{background:radial-gradient(ellipse 22px 40px at 90px 78px,#dedede 0,#b8b8b8 60%,rgba(184,184,184,0) 100%),radial-gradient(ellipse 26px 16px at 120px 118px,#2a2a2a 0,rgba(42,42,42,0) 100%),#fbfbf9}
.photo-plant{background:radial-gradient(ellipse 30px 30px at 97px 62px,#8fb64f 0,rgba(143,182,79,0) 100%),radial-gradient(ellipse 32px 48px at 97px 100px,#ffffff 0,#e2e2e2 70%,rgba(226,226,226,0) 100%),#fbfbf9}
.photo-tubes{background:radial-gradient(ellipse 22px 60px at 85px 80px,#f1f4e6 0,#d9e3c0 70%,rgba(217,227,192,0) 100%),radial-gradient(ellipse 20px 50px at 115px 90px,#f1f4e6 0,#d6e0bb 70%,rgba(214,224,187,0) 100%),#fbfbf9}
.card-foot{height:86px;background:var(--card-foot);display:flex;align-items:center;justify-content:space-between;padding:0 8px;border-top:1px solid #e3e3e3}
.card-name{font-size:12px;font-weight:700;color:var(--ink);line-height:16px}
.price{width:42px;height:40px;background:var(--green);color:#fff;font-size:13px;display:flex;align-items:center;justify-content:center}
.view-more{left:311px;top:1882px;width:840px;display:flex;align-items:center;gap:18px;font-size:12px;font-weight:700;color:var(--green)}
.view-more i{flex:1;height:8px;border-top:2px dotted #cfcfcf;border-bottom:2px dotted #cfcfcf}

/* banner */
.banner{left:0;top:1959px;width:1200px;height:401px;background:
  radial-gradient(ellipse 120px 200px at 920px 260px,#f6f3ee 0,#e8e2da 55%,rgba(232,226,218,0) 100%),
  radial-gradient(ellipse 40px 50px at 940px 70px,#4a3a30 0,rgba(74,58,48,0) 100%),
  linear-gradient(180deg,rgba(0,0,0,0) 75%,#b9c1c2 85%,#9ea8a8 100%),
  linear-gradient(180deg,#97b8d8 0,#b9cfe3 50%,#dbe4ea 75%,#cfd6d6 100%)}
.banner-title{left:97px;top:2054px;font-family:"Cinzel",Georgia,serif;font-size:32px;line-height:48px;color:var(--ink)}
.btn{height:46px;display:flex;align-items:center;justify-content:center;font-size:14px;font-weight:700;letter-spacing:.5px}
.btn-green{background:var(--green);color:#fff}
.btn-silver{background:linear-gradient(180deg,#f4f4f4,#c9c9c9);color:var(--ink)}

/* HQ band */
.hq{left:0;top:2360px;width:1200px;height:424px;background:
  radial-gradient(ellipse 260px 200px at 170px 180px,#d9d2b8 0,rgba(217,210,184,0) 100%),
  radial-gradient(ellipse 200px 120px at 480px 60px,#c0b59a 0,rgba(192,181,154,0) 100%),
  linear-gradient(100deg,#aeb47f 0,#9cb35c 35%,#86aa3e 65%,#a2bd68 100%)}
.hq-title{left:0;top:2414px;width:1200px;text-align:center;font-family:"Cinzel",Georgia,serif;font-size:23px;color:#fff}
.hq-copy{left:160px;top:2458px;width:880px;text-align:center;font-size:12px;line-height:24px;color:#fff}
.book-box{width:264px;height:68px;border:2px solid rgba(255,255,255,.85);color:#fff;text-align:center;font-family:"Cinzel",Georgia,serif;padding-top:12px}
.book-box small{display:block;font-size:11px}
.book-box b{display:block;font-weight:400;font-size:17px;margin-top:2px}

/* map */
.map{left:0;top:2784px;width:1200px;height:375px;background:
  radial-gradient(ellipse 420px 240px at 120px 300px,#dcdcdc 0,rgba(220,220,220,0) 100%),
  radial-gradient(ellipse 500px 260px at 900px 120px,#d2d2d2 0,rgba(210,210,210,0) 100%),
  radial-gradient(ellipse 300px 180px at 620px 200px,#c9c9c9 0,rgba(201,201,201,0) 100%),
  linear-gradient(160deg,#ededed,#dedede 50%,#e7e7e7)}
.zoom{left:1160px;top:3090px;width:26px;height:52px;background:#fff;box-shadow:0 1px 3px rgba(0,0,0,.3);font-size:16px;text-align:center;line-height:26px;color:#555}

/* footer */
.footer{left:0;top:3159px;width:1200px;height:150px;background:var(--footer)}
.footer-row{top:3178px;display:flex;align-items:center;gap:10px;font-size:12px;color:#e6e6e6}
.footer-links{left:0;top:3238px;width:1200px;text-align:center;font-size:12px;color:#e6e6e6;word-spacing:2px}
.copyright{left:0;top:3261px;width:1200px;text-align:center;font-size:12px;color:#cfcfcf}
.foot-dot{width:12px;height:12px;border-radius:50%;background:#e6e6e6;margin-left:14px}
</style>
</head>
<body>

<!-- header -->
<div class="abs topline"></div>
<div class="abs brand"><span class="brand-square"></span><span class="brand-name">Meridel Wellness</span></div>
<div class="abs contacts">
  <span class="social-dot" style="background:#3b5c9a"></span>
  <span class="social-dot" style="background:#2fa8e0"></span>
  <span class="social-dot" style="background:#d3202a"></span>
  <span class="contact-item">
    <svg width="28" height="28" viewBox="0 0 28 28"><circle cx="14" cy="14" r="13" fill="var(--green)"/><path d="M10 8l3 3-2 2c1 2 2 3 4 4l2-2 3 3-2 2c-5 0-10-5-10-10z" fill="#fff"/></svg>
    844-555-0192</span>
  <span class="contact-item">
    <svg width="28" height="28" viewBox="0 0 28 28"><circle cx="14" cy="14" r="13" fill="var(--green)"/><rect x="8" y="9" width="12" height="10" fill="#fff"/><path d="M8 9l6 5 6-5" stroke="var(--green)" fill="none"/></svg>
    care@meridelwellness.example</span>
</div>
<nav class="abs main-nav">
  <span class="active">Home</span><span>About</span><span>Services</span><span>Conditions Treated</span><span>Nutrition</span><span>Therapy ▾</span><span>Essential Oils</span><span>Vitamin</span><span>Events</span><span>Support</span><span>Store</span><span>Blog</span><span>Contact</span>
</nav>
<svg class="abs search" width="16" height="16" viewBox="0 0 16 16"><circle cx="6.5" cy="6.5" r="4.5" stroke="#222" stroke-width="2" fill="none"/><path d="M10 10l4 4" stroke="#222" stroke-width="2"/></svg>

<!-- side rail -->
<aside class="abs rail">
  <div class="rail-head" style="top:4px">NAVIGATIONS</div>
  <ul class="rail-list" style="top:38px">
    <li>Meridel Wellness Store</li><li>Meridel Nutrition</li><li>Nutrient Therapy</li><li>Herbal Apothecary</li><li>Essential Oils</li><li>Vitamins, Minerals, Supplements</li><li>Forest &amp; Nature Therapy</li><li>Meridel Therapies</li><li>Retreats Colorado</li><li>Retreats Hawaii</li><li>Retreats California</li><li>Glamping Camps</li><li>Conditions We Treat</li><li>Support Groups</li><li>Events</li><li>Blog</li><li>Contact</li><li>Home</li><li>Book A Nutrition Consult</li><li>Book A Herbal Therapy Consult</li><li>Book A Forest Therapy Session</li><li>Book An Outdoor Therapy Consult</li><li>Book A Luxury Retreat</li><li>Book A Glamping Camp</li>
  </ul>
  <div class="rail-head" style="top:1226px">IMPOTENCE</div>
  <ul class="rail-list" style="top:1264px">
    <li>Autoimmune Diseases</li><li>Weight Loss/Weight Gain</li><li>Hormonal Issues</li><li>Insomnia</li><li>ADD/ADHD</li><li>Anxiety</li><li>Autism</li><li>Alzheimer's Disease</li><li>Bipolar</li><li>Depression</li><li>Post-Partum Depression</li><li>Schizophrenia</li><li>Alzheimer's disease</li><li>Behavioral disorders</li><li>Pyrrole disorder</li><li>Learning disorders</li><li>Eating disorders</li>
  </ul>
</aside>
<div class="abs rail-video" role="img" aria-label="Video still of a forest lake among pine trees"></div>
<div class="abs rail-video-title">Meridel Wellness</div>
<svg class="abs rail-video-tools" width="42" height="16" viewBox="0 0 42 16"><circle cx="8" cy="8" r="6" stroke="#fff" stroke-width="1.6" fill="none"/><path d="M8 4v4l3 2" stroke="#fff" stroke-width="1.6" fill="none"/><path d="M26 12c1-5 5-7 10-7V2l5 5-5 5V9c-4 0-7 1-10 3z" fill="#fff"/></svg>
<svg class="abs play" width="34" height="34" viewBox="0 0 34 34"><circle cx="17" cy="17" r="16" fill="rgba(0,0,0,.45)"/><path d="M13 10l11 7-11 7z" fill="#fff"/></svg>
<div class="abs rail-promo" role="img" aria-label="Woman with open arms in a flowering meadow"></div>
<div class="abs rail-promo-panel"></div>
<div class="abs rail-promo-text">Meridel Wellness Est. Aspen Colorado with locations in Aspen/Vail Colorado, Hawaii and California.</div>

<!-- hero -->
<div class="abs hero" role="img" aria-label="Close-up of white orchid flowers with water drops"></div>
<div class="abs hero-title">MERIDEL VERDANT<br>REMEDIALS</div>
<div class="abs dots"><span></span><span></span><span></span><span></span></div>

<!-- welcome -->
<div class="abs badge" style="left:726px;top:508px"></div>
<h1 class="abs section-title" style="top:574px;font-size:22px;font-weight:400">Welcome to Meridel Wellness</h1>
<p class="abs welcome-text" style="top:618px">We sell luxury all-natural and prescription drug-FREE brand, Meridel Verdant Remedials located in Est. Aspen, Colorado with branches in Vail, California, Hawai</p>
<p class="abs welcome-text" style="top:678px">We deliver phytoncide and plant medicines as well as essential oils, vitamins, supplements, minerals, herbs, other skin, cosmetic, beauty products, products for the home and office, pet products and health products along with the following services</p>

<!-- services -->
<div class="abs rule" style="top:778px"></div>
<div class="abs badge" style="left:726px;top:766px"></div>
<h2 class="abs section-title" style="top:834px;font-size:22px;font-weight:400">Our Services</h2>

<div class="abs service" style="left:303px;top:893px">
  <div class="service-icon"><svg width="76" height="76" viewBox="0 0 76 76"><circle cx="38" cy="42" r="15" fill="#fff"/><path d="M38 27c2-6 6-8 10-8-1 5-5 8-10 8z" fill="#fff"/></svg></div>
  <div class="service-name">NUTRITION<br>COUNSELING</div>
  <div class="service-copy">And deliver allnatural plant based therapeutic treatments to heal, reverse or prevent</div>
  <div class="read-more">READ MORE &gt;&gt;</div>
</div>
<div class="abs service" style="left:522px;top:893px">
  <div class="service-icon"><svg width="76" height="76" viewBox="0 0 76 76"><rect x="18" y="30" width="38" height="17" rx="8.5" fill="#fff" transform="rotate(-35 37 38)"/><circle cx="51" cy="50" r="9" fill="#fff" stroke="var(--green)" stroke-width="2"/><path d="M51 45v10M46 50h10" stroke="var(--green)" stroke-width="2.5"/></svg></div>
  <div class="service-name">NUTRIENT<br>THERAPY</div>
  <div class="service-copy">And deliver allnatural plant based therapeutic treatments to heal, reverse or prevent</div>
  <div class="read-more">READ MORE &gt;&gt;</div>
</div>
<div class="abs service" style="left:740px;top:893px">
  <div class="service-icon"><svg width="76" height="76" viewBox="0 0 76 76"><path d="M18 36h40c0 12-9 20-20 20s-20-8-20-20z" fill="#fff"/><rect x="40" y="16" width="6" height="22" rx="3" fill="#fff" transform="rotate(30 43 27)"/></svg></div>
  <div class="service-name">HERBALISM</div>
  <div class="service-copy">And deliver allnatural plant based therapeutic treatments to heal, reverse or prevent</div>
  <div class="read-more" style="margin-top:32px">READ MORE &gt;&gt;</div>
</div>
<div class="abs service" style="left:961px;top:893px">
  <div class="service-icon"><svg width="76" height="76" viewBox="0 0 76 76"><rect x="34" y="14" width="8" height="10" fill="#fff"/><rect x="26" y="26" width="24" height="34" rx="4" fill="#fff"/></svg></div>
  <div class="service-name">HERBALISM<br>FORMULAS</div>
  <div class="service-copy">And deliver allnatural plant based therapeutic treatments to heal, reverse or prevent</div>
  <div class="read-more">READ MORE &gt;&gt;</div>
</div>

<!-- products -->
<div class="abs rule" style="top:1196px"></div>
<div class="abs badge" style="left:726px;top:1180px"></div>
<h2 class="abs section-title" style="top:1244px;font-size:21px;font-weight:400">We deliver phytoncide and plant medicines</h2>
<svg class="abs" style="left:724px;top:1285px" width="36" height="16" viewBox="0 0 36 16"><circle cx="8" cy="8" r="7" fill="var(--green)"/><path d="M10 4l-4 4 4 4" stroke="#fff" stroke-width="2" fill="none"/><circle cx="28" cy="8" r="7" fill="var(--green)"/><path d="M26 4l4 4-4 4" stroke="#fff" stroke-width="2" fill="none"/></svg>

<div class="abs card" style="left:311px;top:1339px"><div class="card-photo photo-bottle" role="img" aria-label="White supplement bottle"></div><div class="card-foot"><span class="card-name">Meridel Verdant<br>Remedials</span><span class="price">$40</span></div></div>
<div class="abs card" style="left:527px;top:1339px"><div class="card-photo photo-jar" role="img" aria-label="Small white supplement jar"></div><div class="card-foot"><span class="card-name">Meridel Verdant<br>Remedials</span><span class="price">$40</span></div></div>
<div class="abs card" style="left:741px;top:1339px"><div class="card-photo photo-box" role="img" aria-label="White product gift box"></div><div class="card-foot"><span class="card-name">Meridel Verdant<br>Remedials</span><span class="price">$40</span></div></div>
<div class="abs card" style="left:957px;top:1339px"><div class="card-photo photo-dropper" role="img" aria-label="Essential oil dropper bottle"></div><div class="card-foot"><span class="card-name">Meridel Verdant<br>Remedials</span><span class="price">$40</span></div></div>
<div class="abs card" style="left:311px;top:1604px"><div class="card-photo photo-plant" role="img" aria-label="Jar with green plant label"></div><div class="card-foot"><span class="card-name">Meridel Verdant<br>Remedials</span><span class="price">$40</span></div></div>
<div class="abs card" style="left:527px;top:1604px"><div class="card-photo photo-tubes" role="img" aria-label="Two cream tubes"></div><div class="card-foot"><span class="card-name">Meridel Verdant<br>Remedials</span><span class="price">$40</span></div></div>
<div class="abs card" style="left:741px;top:1604px"><div class="card-photo photo-plant" role="img" aria-label="Jar with green plant label"></div><div class="card-foot"><span class="card-name">Meridel Verdant<br>Remedials</span><span class="price">$40</span></div></div>
<div class="abs card" style="left:957px;top:1604px"><div class="card-photo photo-box" role="img" aria-label="White product gift box"></div><div class="card-foot"><span class="card-name">Meridel Verdant<br>Remedials</span><span class="price">$40</span></div></div>

<svg class="abs" style="left:311px;top:1339px" width="420" height="250" viewBox="0 0 420 250">
  <g id="ribbon"><path d="M0 0h30L0 30z M56 0h30L0 86V56z" fill="var(--green)"/><text x="12" y="45" transform="rotate(-45 28 40)" font-family="Open Sans, sans-serif" font-size="10" fill="#fff">Shop Now</text></g>
  <use href="#ribbon" x="216"/>
</svg>
<svg class="abs" style="left:741px;top:1339px" width="420" height="250" viewBox="0 0 420 250"><use href="#ribbon"/><use href="#ribbon" x="216"/></svg>
<svg class="abs" style="left:311px;top:1604px" width="420" height="250" viewBox="0 0 420 250"><use href="#ribbon"/><use href="#ribbon" x="216"/></svg>
<svg class="abs" style="left:741px;top:1604px" width="420" height="250" viewBox="0 0 420 250"><use href="#ribbon"/><use href="#ribbon" x="216"/></svg>

<div class="abs view-more"><i></i><span>VIEW MORE &gt;&gt;</span><i></i></div>

<!-- booking banner -->
<div class="abs banner" role="img" aria-label="Woman in a white dress raising her arms before mountains and sky"></div>
<div class="abs badge" style="left:590px;top:1922px"></div>
<h2 class="abs banner-title">Recreational therapy or<br>nutrition or herbalism<br>consults</h2>
<div class="abs btn btn-green" style="left:97px;top:2234px;width:272px">BOOK ONLINE CONSULTATION</div>
<div class="abs btn btn-silver" style="left:393px;top:2234px;width:270px">APPOINTMENT BOOKING</div>

<!-- HQ band -->
<div class="abs hq" role="img" aria-label="Woman resting in green grass, soft green overlay"></div>
<h2 class="abs hq-title">We are HQ in Aspen Colorado with locations in Vail, California, Hawaii...</h2>
<p class="abs hq-copy">We heal, reverse and prevent chronic illness and disease naturally without pharmaceutical drugs of any kind. Our main firm is a concierge medical firm which offers concierge medical services to high net worth clients, executives, families, kids and corporations</p>
<div class="abs book-box" style="left:170px;top:2543px"><small>Book an Appointment for</small><b>Recreational Therapy</b></div>
<div class="abs book-box" style="left:470px;top:2543px"><small>Book an Appointment for</small><b>Nutrition</b></div>
<div class="abs book-box" style="left:770px;top:2543px"><small>Book an Appointment for</small><b>Herbalism Consults</b></div>
<div class="abs book-box" style="left:470px;top:2657px"><small>Book an Appointment for</small><b>Luxury Retreat</b></div>

<!-- map -->
<div class="abs map" role="img" aria-label="Greyscale map of southern California with two location pins"></div>
<svg class="abs" style="left:393px;top:2868px" width="16" height="22" viewBox="0 0 16 22"><path d="M8 0a8 8 0 0 1 8 8c0 6-8 14-8 14S0 14 0 8a8 8 0 0 1 8-8z" fill="#d12a2a"/><circle cx="8" cy="8" r="3" fill="#fff"/></svg>
<svg class="abs" style="left:778px;top:3090px" width="16" height="22" viewBox="0 0 16 22"><path d="M8 0a8 8 0 0 1 8 8c0 6-8 14-8 14S0 14 0 8a8 8 0 0 1 8-8z" fill="#d12a2a"/><circle cx="8" cy="8" r="3" fill="#fff"/></svg>
<div class="abs zoom">+<br>−</div>

<!-- footer -->
<footer class="abs footer"></footer>
<div class="abs footer-row" style="left:98px"><svg width="12" height="16" viewBox="0 0 12 16"><path d="M6 0a6 6 0 0 1 6 6c0 4-6 10-6 10S0 10 0 6a6 6 0 0 1 6-6z" fill="#e6e6e6"/><circle cx="6" cy="6" r="2" fill="var(--footer)"/></svg>23 Building name, Street name, City - Zipcode</div>
<div class="abs footer-row" style="left:478px"><svg width="14" height="14" viewBox="0 0 14 14"><path d="M2 1l3 3-1.5 1.5c1 2 2.5 3.5 4.5 4.5L9.5 8.5l3 3-2 2C5 13.5.5 9 .5 3z" fill="#e6e6e6"/></svg>844-555-0192</div>
<div class="abs footer-row" style="left:688px"><svg width="16" height="12" viewBox="0 0 16 12"><rect width="16" height="12" fill="#e6e6e6"/><path d="M0 0l8 6 8-6" stroke="var(--footer)" fill="none"/></svg>care@meridelwellness.example</div>
<div class="abs footer-row" style="left:980px"><span class="foot-dot"></span><span class="foot-dot"></span><span class="foot-dot"></span><span class="foot-dot"></span></div>
<div class="abs footer-links">Home &nbsp;|&nbsp; Meridel Wellness Store &nbsp;|&nbsp; Glamping Health Camps &nbsp;|&nbsp; Contact &nbsp;|&nbsp; About &nbsp;|&nbsp; Blog</div>
<div class="abs copyright">Copyright © 2016 Meridel Wellness. All rights reserved.</div>

</body>
</html>
```